General Dental Office Business Card

I run a private general dental office in southern California, and would like a refresh/redesign of my business card. I focus on quality care rather than volume. The email address on the uploaded current card should be updated to: info@marbleshoredental.example. The current card's logo is a deboss, but I am open to other ideas. The logo can be refreshed, but it is something that's been with me since the beginning of the office, so I wouldn't want a drastic redesign.
Target Market(s)
Adults 18-99, whoever needs dental services
Industry/Entity Type
Healthcare/Dental
Contact Information for Business Card
Name, Address, Phone, email
Colors
Designer to choose colors to be used in the design.
Requirements
Must have
- Logo (Same as original one in the uploaded file), space on back for appointment time/date

```html
<!DOCTYPE html>
<html lang="en">
<head>
<meta charset="utf-8">
<title>Marble Shore Dental – Business Card</title>
<link href="https://fonts.googleapis.com/css2?family=Lato:ital,wght@0,400;0,700;0,900;1,400&display=swap" rel="stylesheet">
<style>
  :root {
    --teal: #36b8c6;
    --teal-light: #74cdd8;
    --ink: #333a3d;
    --paper: #ffffff;
    --stage: #2d2d2f;
  }
  * { box-sizing: border-box; margin: 0; padding: 0; }
  html, body { width: 1200px; height: 875px; overflow: hidden; }
  body {
    background: var(--stage);
    font-family: 'Lato', sans-serif;
    position: relative;
  }
  .card {
    position: absolute;
    width: 560px;
    height: 320px;
    background: var(--paper);
    border-radius: 20px;
    overflow: hidden;
    box-shadow: 0 20px 40px rgba(0,0,0,.45);
  }

  /* ---------- Back: appointment ---------- */
  .card-back { left: 30px; top: 170px; padding: 30px 36px 0; }
  .appt-title {
    text-align: center;
    color: var(--teal);
    font-weight: 700;
    font-size: 27px;
    letter-spacing: .5px;
    margin-bottom: 22px;
  }
  .field-row { display: flex; align-items: flex-end; margin-bottom: 16px; font-size: 14px; }
  .label { color: var(--teal); text-transform: uppercase; letter-spacing: .5px; }
  .fill { flex: 1; border-bottom: 1.5px dotted #555; margin: 0 4px 3px; }
  .fill.short { flex: 0 0 170px; }
  .days { display: flex; justify-content: space-between; margin: 4px 14px 16px 40px; font-size: 14px; color: var(--ink); }
  .day { display: flex; align-items: center; gap: 5px; }
  .box { width: 13px; height: 13px; border: 1.6px solid var(--teal); }
  .blank-line { border-bottom: 1.5px dotted #555; margin: 6px 0 16px; }
  .fine-print { text-align: center; font-style: italic; font-size: 11.5px; color: var(--ink); line-height: 1.35; }

  /* ---------- Front: identity ---------- */
  .card-front { left: 610px; top: 390px; }
  .card-front svg.wave { position: absolute; inset: 0; }
  .identity { position: absolute; left: 30px; top: 138px; color: var(--paper); }
  .doctor-name { font-weight: 900; font-size: 21px; letter-spacing: .3px; white-space: nowrap; }
  .specialty { font-size: 14px; margin-bottom: 12px; }
  .contact { list-style: none; font-size: 13px; line-height: 1.35; }
  .contact li { display: flex; gap: 9px; align-items: flex-start; margin-bottom: 3px; }
  .contact svg { width: 12px; height: 12px; flex: 0 0 12px; margin-top: 3px; fill: var(--paper); }
  .brand { position: absolute; left: 322px; top: 96px; display: flex; align-items: center; gap: 11px; color: var(--teal); }
  .brand-dot { width: 46px; height: 46px; border-radius: 50%; border: 3px solid var(--teal); flex: 0 0 46px; }
  .brand-name { font-size: 18px; font-weight: 400; line-height: 1.1; letter-spacing: .5px; text-transform: uppercase; white-space: nowrap; }
</style>
</head>
<body>

<section class="card card-back" aria-label="Appointment card back">
  <h2 class="appt-title">NEXT APPOINTMENT</h2>
  <div class="field-row"><span class="label">Name</span><span class="fill"></span></div>
  <div class="field-row">
    <span class="label">Date</span><span class="fill"></span>
    <span class="label">Time</span><span class="fill short"></span>
    <span class="label">AM\PM</span>
  </div>
  <div class="days">
    <span class="day"><span class="box"></span>MON</span>
    <span class="day"><span class="box"></span>TUES</span>
    <span class="day"><span class="box"></span>WED</span>
    <span class="day"><span class="box"></span>THU</span>
    <span class="day"><span class="box"></span>FRI</span>
    <span class="day"><span class="box"></span>SAT</span>
  </div>
  <div class="field-row"><span class="label">Comments</span><span class="fill"></span></div>
  <div class="blank-line"></div>
  <p class="fine-print">If you are unable to keep your appointment, please call us to<br>reschedule at least 48 hours prior to your appointment.</p>
</section>

<section class="card card-front" aria-label="Business card front">
  <svg class="wave" viewBox="0 0 560 320" width="560" height="320">
    <path d="M0 0 H276 C290 200 424 300 528 320 H0 Z" fill="var(--teal-light)"/>
    <path d="M0 0 H268 C282 202 414 302 514 320 H0 Z" fill="var(--paper)"/>
    <path d="M0 0 H262 C276 204 412 304 512 320 H0 Z" fill="var(--teal)"/>
  </svg>

  <div class="identity">
    <h1 class="doctor-name">DANIEL R. MOSS DDS</h1>
    <p class="specialty">General Dentistry</p>
    <ul class="contact">
      <li><svg viewBox="0 0 12 12"><path d="M6 0a4 4 0 0 0-4 4c0 3 4 8 4 8s4-5 4-8a4 4 0 0 0-4-4zm0 5.5A1.5 1.5 0 1 1 6 2.5a1.5 1.5 0 0 1 0 3z"/></svg><span>2180 Harbor View Lane<br>Coastview, CA 92600</span></li>
      <li><svg viewBox="0 0 12 12"><path d="M2.5 0.5l2 2.5-1.2 1.3a7 7 0 0 0 4.4 4.4L9 7.5l2.5 2-1.3 2C5 11.5 0.5 7 0.5 1.8z"/></svg><span>555-014-2828</span></li>
      <li><svg viewBox="0 0 12 12"><path d="M0 2h12v8H0z M0 2l6 4.5L12 2" stroke="var(--teal)" stroke-width="1"/></svg><span>info@marbleshoredental.example</span></li>
      <li><svg viewBox="0 0 12 12"><circle cx="6" cy="6" r="5.5"/><path d="M0.5 6h11M6 0.5c-3 3-3 8 0 11M6 0.5c3 3 3 8 0 11" stroke="var(--teal)" stroke-width=".8" fill="none"/></svg><span>marbleshoredental.example</span></li>
    </ul>
  </div>

  <div class="brand">
    <span class="brand-dot"></span>
    <span class="brand-name">Marble<br>Shore Dental</span>
  </div>
</section>

</body>
</html>
```